Brantley Advisory Group provides support for renewable energy projects to utilities and suppliers

I need a professional looking business card that is both simple and elegant and unique. My clients are mostly large organizations not individuals. I am a consultant with my own company that is small but would like to give clients the impression I am larger. Smart grid, fiber optics, software, field hardware, distribution automation, substation automation, operations, energy storage/batteries, microgrids, customer service, strategy/roadmaps, conservation, Automated Metering Infrastruture (AMI or smart meters) are all areas of focus.

Target Market(s)

Utilities, suppliers, governmental agencies involved in energy. All types of energy especially natural gas and electrical. Especially renewable energy or green projects.

Contact Information for Business Card

Name - Mark Brantley Cell Phone - 425.318.2746 Email - mbrantley@brantleyag-example.com
Company - Brantley Advisory Group (logo) Title - Principal

Font styles to use
Serif
Sans Serif

Colors

Designer to choose colors to be used in the design.

Requirements
Must have
• Simple and professional and powerful.
• Unique/creative design.
Nice to have
• Utilize color scheme to accent logo colors. Maybe some geometric pattern on edge of card with color.
Should not have
• Busy, complicated, traditional

```html
<!DOCTYPE html>
<html lang="en">
<head>
<meta charset="utf-8">
<title>Brantley Advisory Group – Business Card</title>
<link rel="stylesheet" href="https://fonts.googleapis.com/css2?family=Montserrat:wght@400;500;600&display=swap">
<style>
  :root {
    --backdrop: #b4b4b4;
    --card: #f7f7f7;
    --navy: #1f3a93;
    --green: #4e8a2a;
    --ink: #444444;
    --muted: #555555;
  }
  * { margin: 0; padding: 0; box-sizing: border-box; }
  html, body {
    width: 1200px;
    height: 750px;
    overflow: hidden;
    background: var(--backdrop);
    font-family: "Montserrat", Arial, sans-serif;
  }
  .canvas {
    position: relative;
    width: 1200px;
    height: 750px;
  }
  .card {
    position: absolute;
    top: 226px;
    width: 501px;
    height: 286px;
    background: var(--card);
    border-radius: 16px;
    overflow: hidden;
  }
  .card--front { left: 90px; }
  .card--back { left: 612px; }

  /* Front */
  .brand {
    position: absolute;
    left: 39px;
    top: 38px;
    display: flex;
    align-items: center;
    gap: 10px;
  }
  .brand__mark {
    width: 30px;
    height: 30px;
    border: 2px solid var(--navy);
    border-radius: 4px;
  }
  .brand__name {
    font-weight: 600;
    font-size: 15px;
    line-height: 1.2;
    color: var(--navy);
  }
  .divider {
    position: absolute;
    left: 39px;
    top: 162px;
    width: 17px;
    height: 2px;
    background: var(--navy);
  }
  .person {
    position: absolute;
    left: 39px;
    top: 175px;
  }
  .person__name {
    font-weight: 500;
    font-size: 15px;
    color: var(--navy);
  }
  .person__title {
    font-size: 12px;
    color: var(--green);
    margin-top: 1px;
  }
  .contact {
    position: absolute;
    left: 39px;
    top: 225px;
    list-style: none;
    font-size: 10.5px;
    color: var(--ink);
  }
  .contact li {
    display: flex;
    align-items: center;
    gap: 6px;
    height: 15px;
  }
  .contact svg { width: 9px; height: 9px; fill: var(--navy); }
  .website {
    position: absolute;
    right: 30px;
    top: 240px;
    font-size: 10px;
    letter-spacing: 1.2px;
    color: var(--muted);
  }

  /* Back */
  .wordmark {
    position: absolute;
    left: 0;
    right: 0;
    top: 94px;
    padding-left: 160px;
    color: var(--navy);
    font-weight: 600;
  }
  .wordmark__primary {
    display: block;
    font-size: 48px;
    line-height: 1;
    letter-spacing: -0.5px;
  }
  .wordmark__secondary {
    display: block;
    font-size: 21px;
    line-height: 1.4;
    margin-top: 4px;
  }
</style>
</head>
<body>
<main class="canvas">
  <section class="card card--front" aria-label="Business card front">
    <div class="brand">
      <span class="brand__mark" aria-hidden="true"></span>
      <span class="brand__name">Brantley<br>Advisory Group</span>
    </div>

    <span class="divider" aria-hidden="true"></span>

    <div class="person">
      <p class="person__name">Mark Brantley Cell</p>
      <p class="person__title">Principal</p>
    </div>

    <ul class="contact">
      <li>
        <svg viewBox="0 0 24 24" aria-hidden="true"><path d="M6.6 10.8a15.1 15.1 0 0 0 6.6 6.6l2.2-2.2c.3-.3.7-.4 1-.2 1.1.4 2.3.6 3.6.6.6 0 1 .4 1 1V20c0 .6-.4 1-1 1A17 17 0 0 1 3 4c0-.6.4-1 1-1h3.5c.6 0 1 .4 1 1 0 1.3.2 2.5.6 3.6.1.3 0 .7-.2 1z"/></svg>
        <span>425.318.2746</span>
      </li>
      <li>
        <svg viewBox="0 0 24 24" aria-hidden="true"><path d="M2 5h20v14H2z M3 6l9 7 9-7" /><path d="M2 5l10 8 10-8v14H2z"/></svg>
        <span>mbrantley@brantleyag-example.com</span>
      </li>
    </ul>

    <p class="website">www.brantleyag-example.com</p>
  </section>

  <section class="card card--back" aria-label="Business card back">
    <h1 class="wordmark">
      <span class="wordmark__primary">Brantley</span>
      <span class="wordmark__secondary">Advisory Group</span>
    </h1>
  </section>
</main>
</body>
</html>
```